Velvetorchid Hair & Beauty Business Card

Velvetorchid Hair & Beauty is a boutique salon located in the picturesque Lake Taupo NZ. The salon is very luxurious, opulent gold gilded mirrors, chandelier lit, contemporary french decor, sets the mood to create beautiful hair, makeup and all beauty services. Just had a new logo design and now after a new business card.
Logo
14 Korowhai Street
Taupo
Phone (07) 548 6193
www.velvetorchid.co.nz
email hair@velvetorchid.co.nz
Marlena Swithin
Also need a space to put in Stylist name, date, appointment time. thanks;)
Another idea is we could incorporate the wallpaper in the back ground either on the back or front or use an ornate glided frame (around the edge of the card) like on my website where my brides photos flash.
Decided against the wall paper but at least you can see our colour theme for the salon.
Updates

Please check out my updated brief . Thanks :)

Target Market(s)

25-60 years plus, mainly mid age females , wanting the best possible service , high standard of workmanship and money not a problem.

Industry/Entity Type

Boutique

Requirements
Must have
• Gold and silver

```html
<!DOCTYPE html>
<html lang="en">
<head>
<meta charset="utf-8">
<title>Velvetorchid Hair &amp; Beauty – Business Card</title>
<link href="https://fonts.googleapis.com/css2?family=Questrial&family=Arimo:wght@400&display=swap" rel="stylesheet">
<style>
  :root {
    --page: #ffffff;
    --card: #0c0c0c;
    --card-edge: #1a1a1a;
    --gold: #7a6418;
    --gold-soft: #9a8236;
    --gold-dim: #4a3f22;
    --silver: #e6e6e6;
    --ornament-bright: #8c7434;
    --ornament-faint: #2c271c;
  }
  * { margin: 0; padding: 0; box-sizing: border-box; }
  html, body {
    width: 1200px; height: 1000px; overflow: hidden;
    background: var(--page);
  }
  .sheet { position: relative; width: 1200px; height: 1000px; }

  .card {
    position: absolute;
    width: 530px; height: 924px;
    background: radial-gradient(ellipse at 50% 45%, #141414 0%, var(--card) 70%);
    border: 1px solid var(--card-edge);
    overflow: hidden;
  }
  .card--front { left: 27px; top: 35px; }
  .card--back  { left: 641px; top: 37px; }

  /* ornament placeholders */
  .ornament {
    position: absolute;
    border-radius: 50% 50% 40% 40% / 60% 60% 40% 40%;
  }
  .ornament--crest {
    left: 108px; top: 373px; width: 296px; height: 70px;
    background: radial-gradient(ellipse at 50% 55%, var(--ornament-bright) 0%, rgba(140,116,52,0.35) 55%, rgba(140,116,52,0) 75%);
  }
  .ornament--footer {
    left: 28px; top: 772px; width: 476px; height: 118px;
    background: radial-gradient(ellipse at 50% 60%, var(--ornament-faint) 0%, rgba(44,39,28,0.5) 50%, rgba(44,39,28,0) 75%);
  }

  /* brand lockup */
  .brand {
    position: absolute; left: 0; top: 462px; width: 530px;
    text-align: center;
    font-family: "Questrial", sans-serif;
    font-weight: 400;
    color: var(--gold-soft);
  }
  .brand__name { font-size: 53px; letter-spacing: 0.5px; line-height: 1; }
  .brand__tag {
    display: flex; align-items: center; justify-content: center;
    gap: 8px; margin-top: 14px;
    font-size: 14px; letter-spacing: 1px; text-transform: uppercase;
  }
  .brand__rule { display: block; width: 130px; height: 2px; background: var(--gold); }

  /* back */
  .holder {
    position: absolute; left: 46px; top: 160px;
    font-family: "Questrial", sans-serif;
    font-size: 46px; color: var(--gold); white-space: nowrap;
  }
  .contact {
    position: absolute; left: 172px; top: 270px;
    list-style: none;
    font-family: "Arimo", sans-serif;
    font-size: 25px; line-height: 34px;
    color: var(--silver); white-space: nowrap;
  }
  .appointment {
    position: absolute; left: 47px; top: 584px;
    font-family: "Arimo", sans-serif;
    font-size: 27px; line-height: 42px;
    color: var(--silver);
  }
  .appointment__row { display: flex; }
  .appointment__label { width: 96px; }
</style>
</head>
<body>
<main class="sheet">

  <section class="card card--front" aria-label="Card front">
    <div class="ornament ornament--crest" role="img" aria-label="Gold baroque scrollwork crest above the salon name"></div>
    <div class="brand">
      <div class="brand__name">Velvetorchid</div>
      <div class="brand__tag">
        <span class="brand__rule"></span>
        <span>Hair &amp; Beauty</span>
        <span class="brand__rule"></span>
      </div>
    </div>
    <div class="ornament ornament--footer" role="img" aria-label="Faint gold baroque scrollwork border along the bottom"></div>
  </section>

  <section class="card card--back" aria-label="Card back">
    <h1 class="holder">Marlena Swithin</h1>
    <ul class="contact">
      <li>(07) 548 6193</li>
      <li>14 Korowhai Street, Taupo</li>
      <li>hair@velvetorchid.co.nz</li>
      <li>www.velvetorchid.co.nz</li>
    </ul>
    <div class="appointment">
      <div class="appointment__row"><span class="appointment__label">Stylist</span><span>-</span></div>
      <div class="appointment__row"><span class="appointment__label">Date</span><span>-</span></div>
      <div class="appointment__row"><span class="appointment__label">Time</span><span>-</span></div>
    </div>
    <div class="ornament ornament--footer" role="img" aria-label="Faint gold baroque scrollwork border along the bottom"></div>
  </section>

</main>
</body>
</html>
```